Flyer Design Project

Training and Consulting Flyer

I attached a document that contained the wording for the flyer as well as the logo.

Target Market(s)

Little Compass agencies and grantees

Industry/Entity Type

Training

Font styles to use
Sans Serif

Colors
e667a6
eda3c7
a54499
b768aa
f9d9e8

Requirements
Must have
• Words provided on attachment
Nice to have
• Graphics that are related to adult training/learning and consulting

```html
<!DOCTYPE html>
<html lang="en">
<head>
<meta charset="utf-8">
<title>MERA Health Consultants – Training and Consulting Flyer</title>
<link rel="stylesheet" href="https://fonts.googleapis.com/css2?family=Arimo:wght@400;700&family=Oswald:wght@400;500;600&family=Montserrat:wght@700;800&display=swap">
<style>
  :root {
    --magenta: #b21f6c;
    --magenta-soft: #c4528f;
    --ink: #141414;
    --paper: #ffffff;
    --backdrop: #e9e6e4;
    --photo-light: #eeeeee;
    --photo-dark: #5c5c5c;
    --font-body: "Arimo", Arial, sans-serif;
    --font-display: "Oswald", "Arial Narrow", sans-serif;
    --font-name: "Montserrat", Arial, sans-serif;
  }
  * { box-sizing: border-box; margin: 0; padding: 0; }
  html, body { width: 1200px; height: 840px; overflow: hidden; }
  body { background: var(--backdrop); font-family: var(--font-body); position: relative; }

  .page { position: absolute; top: 82px; width: 526px; height: 675px; }
  .page--front { left: 71px; background: var(--paper); }
  .page--back { left: 603px; background: var(--magenta); }
  .page > * { position: absolute; }

  /* Front page */
  .header-band { left: 63px; top: 65px; width: 398px; height: 126px; background: var(--magenta); }
  .header-band__mark { position: absolute; left: 60px; top: 48px; display: flex; align-items: center; gap: 8px;
    font-family: var(--font-display); font-weight: 500; font-size: 22px; color: var(--paper); letter-spacing: 1px; }
  .header-band__mark::before { content: ""; width: 18px; height: 18px; border-radius: 50%; background: var(--paper); }
  .header-band__lines { position: absolute; left: 236px; top: 10px; font-family: var(--font-display); font-weight: 500;
    font-size: 15px; line-height: 15px; color: var(--paper); text-transform: uppercase; }
  .header-band__lines p + p { margin-top: 0; }
  .header-band__gap { height: 9px; }

  .photo { background: linear-gradient(160deg, var(--photo-light) 0%, #c9c9c9 45%, var(--photo-dark) 100%); }
  .photo--team { left: 63px; top: 191px; width: 398px; height: 241px; }

  .brand-lockup { left: 214px; top: 451px; display: flex; align-items: center; gap: 16px; }
  .brand-lockup__dot { width: 58px; height: 58px; border-radius: 50%; background: var(--magenta); }
  .brand-lockup__name { font-family: var(--font-display); font-weight: 500; font-size: 27px; line-height: 29px;
    color: var(--ink); text-transform: uppercase; letter-spacing: 0.5px; }
  .tagline { left: 247px; top: 545px; font-family: var(--font-body); font-size: 16px; color: var(--ink); letter-spacing: 0.5px; }

  .contact { width: 246px; }
  .contact__email { font-size: 9px; color: var(--magenta); }
  .contact__phone { font-size: 10px; font-weight: 700; letter-spacing: 1.2px; margin-top: 3px; }
  .contact__address { margin-top: 6px; height: 22px; padding-left: 8px; font-size: 8px; font-weight: 700; line-height: 22px; }
  .page--front .contact { left: 304px; top: 576px; width: 157px; }
  .page--front .contact__phone { color: var(--ink); }
  .page--front .contact__address { background: var(--magenta); color: var(--paper); }

  .person { top: 605px; padding-left: 8px; border-left: 2px solid; font-family: var(--font-name); font-weight: 800;
    font-size: 13px; line-height: 20px; letter-spacing: 0.3px; }
  .page--front .person { left: 63px; color: var(--magenta); border-color: var(--magenta); }

  /* Back page */
  .photo--office { left: 56px; top: 65px; width: 398px; height: 126px; }
  .vertical-slogan { left: 56px; top: 268px; width: 300px; height: 132px; transform-origin: 0 0;
    transform: translateY(300px) rotate(-90deg); font-family: var(--font-display); font-weight: 600; font-size: 62px;
    line-height: 62px; color: var(--magenta-soft); text-transform: uppercase; letter-spacing: 1px; }
  .copy { left: 207px; top: 195px; width: 247px; font-size: 11px; line-height: 12px; color: var(--paper); text-align: justify; }
  .copy p + p { margin-top: 12px; }
  .copy p.copy__tight { margin-top: 0; }
  .rule { left: 207px; top: 564px; width: 246px; height: 2px; background: var(--paper); }
  .page--back .contact { left: 207px; top: 574px; }
  .page--back .contact__email { color: var(--paper); padding-left: 12px; }
  .page--back .contact__phone { color: var(--paper); padding-left: 12px; }
  .page--back .contact__address { background: var(--paper); color: var(--magenta); }
  .page--back .person { left: 30px; color: var(--paper); border-color: var(--paper); }
</style>
</head>
<body>
  <section class="page page--front">
    <div class="header-band">
      <div class="header-band__mark">MERA</div>
      <div class="header-band__lines">
        <p>Method</p><p>Evidence Review</p><p>Analysis</p>
        <div class="header-band__gap"></div>
        <p>Health</p><p>Consultants &amp;</p><p>Group</p>
      </div>
    </div>
    <div class="photo photo--team" role="img" aria-label="Black and white photo of a business team meeting around a table"></div>
    <div class="brand-lockup">
      <span class="brand-lockup__dot"></span>
      <div class="brand-lockup__name">Mera<br>Health<br>Consultants</div>
    </div>
    <p class="tagline">TOGETHER WE CAN</p>
    <div class="contact">
      <p class="contact__email">hello@merahealthadvisors.com</p>
      <p class="contact__phone">(555)-014-2290</p>
      <p class="contact__address">P.O.Box 200, Brookfield, GA 30000</p>
    </div>
    <p class="person">DANA WELLS, CEO</p>
  </section>

  <section class="page page--back">
    <div class="photo photo--office" role="img" aria-label="Black and white photo of a smiling businesswoman with colleagues behind her"></div>
    <div class="vertical-slogan">Together<br>We Can</div>
    <div class="copy">
      <p>Innovative Approaches to meeting the 5 year funding measures in the content area of health, Nutrition, oral Health &amp; Safety.</p>
      <p>MERA health consultant has embarked on a new methodology design to ensure programs meet total requirements as prescribed under the health service program.</p>
      <p>Let us manage your health program through remote and off site measures to ensure total compliance and strategic methodology toward quality service approaches.</p>
      <p>Let us provide consultants to mentor your health manage nutrition content specialist, facilities/ safety manager. Theses support consultant are advanced level academics in their specialized areas of focus.</p>
      <p>Let us provide Evidenced based Mock reviews for your program designed to assist management staff in Focus I, Focus II Review strategies for 2018.</p>
      <p class="copy__tight">Let us provide TITA for any new health nutrition, safety staff to ensure they are fully prepared to perform their job duties at their highest level of management approaches.</p>
    </div>
    <div class="rule"></div>
    <div class="contact">
      <p class="contact__email">hello@merahealthadvisors.com</p>
      <p class="contact__phone">(555)-014-2290</p>
      <p class="contact__address">P.O.Box 200, Brookfield, GA 30000</p>
    </div>
    <p class="person">DANA WELLS, CEO</p>
  </section>
</body>
</html>
```